Quilting Template Retail Label

These are laser cut acrylic templates used to trace shapes onto fabrics. Quilters use these to make repeatable cuts quickly and accurately. Sometimes referred to as quilt rulers. I need to make a label design for my line of products that shows the quality and elegance of these templates. It needs to be an eye catching design as there is stiff competition for the attention of shoppers. Feminine colors are also preferred.

The reference design will be for an item called a "Drunkards Path 7" & 3.5" Set". The label should also say "4 piece set". The brand name is Every Plain Polymer. The Drunkards Path is essentially a Square with a quarter of a circle cut out of it. I would like a dashed line border offset from the edge of the label, that represents the seam allowance. The seam allowance is engraved on all templates.

Pictures of the items are attached, as well as pictures of labels that I would like you to use for inspiration. The picture of the quilt is one of the designs that can be made with the Drunkards Path template. Lastly, there are pictures of the pegboards in shops where these will be displayed, this should give you an idea of the competition.

Target Market(s)

Quilters, older women, affluent

Industry/Entity Type

Retail

Colors
e34297
e667a6
b868aa
d2a4cc

Requirements
Must have
• Must be elegant and give the feeling of a quality product.

```html
<!DOCTYPE html>
<html lang="en">
<head>
<meta charset="utf-8">
<title>Every Plain Polymer – Drunkards Path Labels</title>
<link rel="stylesheet" href="https://fonts.googleapis.com/css2?family=Open+Sans:wght@400;600&family=Lobster+Two:ital,wght@1,700&family=Domine:wght@400;700&display=swap">
<style>
  :root {
    --hot-pink: #e34297;
    --rose: #e667a6;
    --orchid: #b868aa;
    --lilac: #d2a4cc;
    --blush: #f0a3c9;
    --white: #ffffff;
    --subline: #ecd3e8;
  }
  * { margin: 0; padding: 0; box-sizing: border-box; }
  html, body {
    width: 948px;
    height: 1200px;
    overflow: hidden;
    background: var(--white);
  }
  .canvas {
    position: relative;
    width: 948px;
    height: 1200px;
  }

  /* ---------- Label A: dotted bracket frame ---------- */
  .label-bracket {
    position: absolute;
    left: 141px;
    top: 79px;
    width: 664px;
    height: 497px;
  }
  .label-bracket .backdrop {
    position: absolute;
    inset: 0;
    background: var(--hot-pink);
  }
  .label-bracket svg.frame {
    position: absolute;
    inset: 0;
  }
  .label-bracket .content {
    position: absolute;
    inset: 0;
    font-family: "Open Sans", Arial, sans-serif;
    text-align: center;
  }
  .label-bracket .brand {
    position: absolute;
    left: 0; right: 0;
    top: 118px;
    font-size: 36px;
    font-weight: 600;
    color: var(--hot-pink);
  }
  .label-bracket .product-band {
    position: absolute;
    left: 114px;
    top: 235px;
    width: 442px;
    height: 85px;
    border-radius: 28px;
    background: var(--orchid);
    color: var(--white);
  }
  .label-bracket .product-name {
    display: block;
    margin-top: 6px;
    font-size: 39px;
    font-weight: 400;
    line-height: 48px;
    letter-spacing: 0.5px;
  }
  .label-bracket .product-size {
    display: block;
    font-size: 17px;
    font-weight: 600;
    line-height: 20px;
    color: var(--subline);
  }
  .label-bracket .piece-count {
    position: absolute;
    left: 0; right: 0;
    top: 362px;
    font-family: "Lobster Two", "Georgia", cursive;
    font-style: italic;
    font-weight: 700;
    font-size: 30px;
    color: var(--hot-pink);
  }

  /* ---------- Label B: stitched oval frame ---------- */
  .label-oval {
    position: absolute;
    left: 66px;
    top: 618px;
    width: 815px;
    height: 498px;
    background: var(--rose);
  }
  .label-oval .corner-flourish {
    position: absolute;
    width: 154px;
    height: 82px;
    border-radius: 40px;
    background: radial-gradient(ellipse at center, var(--blush) 0%, rgba(240,163,201,0.35) 70%, rgba(240,163,201,0) 100%);
  }
  .label-oval .flourish-tl { left: 28px; top: 18px; }
  .label-oval .flourish-tr { right: 24px; top: 18px; }
  .label-oval .flourish-bl { left: 28px; bottom: 22px; }
  .label-oval .flourish-br { right: 24px; bottom: 22px; }
  .label-oval svg.frame {
    position: absolute;
    inset: 0;
  }
  .label-oval .content {
    position: absolute;
    inset: 0;
    font-family: "Domine", Georgia, serif;
    text-align: center;
  }
  .label-oval .brand {
    position: absolute;
    left: 0; right: 0;
    top: 100px;
    font-size: 32px;
    font-weight: 400;
    color: var(--hot-pink);
  }
  .label-oval .product-name {
    position: absolute;
    left: 0; right: 0;
    top: 213px;
    font-size: 38px;
    font-weight: 700;
    letter-spacing: 3px;
    color: var(--white);
  }
  .label-oval .product-size {
    position: absolute;
    left: 0; right: 0;
    top: 274px;
    font-size: 17px;
    letter-spacing: 1.5px;
    color: var(--white);
  }
  .label-oval .piece-count {
    position: absolute;
    left: 0; right: 0;
    top: 345px;
    font-size: 26px;
    letter-spacing: 2.5px;
    color: var(--hot-pink);
  }
</style>
</head>
<body>
<main class="canvas">

  <section class="label-bracket">
    <div class="backdrop" role="img" aria-label="Hot pink polka dot background pattern"></div>
    <svg class="frame" width="664" height="497" viewBox="0 0 664 497" aria-hidden="true">
      <path fill="#ffffff"
        d="M75 28 Q332 58 589 28 Q636 28 636 75 Q600 248 636 422 Q636 469 589 469 Q332 439 75 469 Q28 469 28 422 Q64 248 28 75 Q28 28 75 28 Z"/>
      <path fill="none" stroke="var(--hot-pink)" stroke-width="4.5" stroke-linecap="round" stroke-dasharray="0 9"
        transform="translate(332 248.5) scale(0.94) translate(-332 -248.5)"
        d="M75 28 Q332 58 589 28 Q636 28 636 75 Q600 248 636 422 Q636 469 589 469 Q332 439 75 469 Q28 469 28 422 Q64 248 28 75 Q28 28 75 28 Z"/>
    </svg>
    <div class="content">
      <p class="brand">Every Plain Polymer</p>
      <div class="product-band">
        <span class="product-name">Drunkards Path</span>
        <span class="product-size">7" &amp; 3.5" Set</span>
      </div>
      <p class="piece-count">4 piece set</p>
    </div>
  </section>

  <section class="label-oval">
    <div class="corner-flourish flourish-tl" role="img" aria-label="Light pink floral flourish ornament"></div>
    <div class="corner-flourish flourish-tr" role="img" aria-label="Light pink floral flourish ornament"></div>
    <div class="corner-flourish flourish-bl" role="img" aria-label="Light pink floral flourish ornament"></div>
    <div class="corner-flourish flourish-br" role="img" aria-label="Light pink floral flourish ornament"></div>
    <svg class="frame" width="815" height="498" viewBox="0 0 815 498" aria-hidden="true">
      <path fill="#ffffff"
        d="M54 116 L180 116 C240 0 575 0 635 116 L763 116 L763 176 C815 200 815 306 763 330 L763 393 L635 393 C575 497 240 497 180 393 L54 393 L54 330 C2 306 2 200 54 176 Z"/>
      <path fill="none" stroke="var(--orchid)" stroke-width="2" stroke-dasharray="9 5"
        transform="translate(407.5 249) scale(0.955 0.93) translate(-407.5 -249)"
        d="M54 116 L180 116 C240 0 575 0 635 116 L763 116 L763 176 C815 200 815 306 763 330 L763 393 L635 393 C575 497 240 497 180 393 L54 393 L54 330 C2 306 2 200 54 176 Z"/>
      <rect x="55" y="200" width="718" height="102" rx="51" fill="var(--orchid)"/>
      <circle cx="92" cy="251" r="12" fill="#ffffff"/>
      <circle cx="735" cy="251" r="12" fill="#ffffff"/>
    </svg>
    <div class="content">
      <p class="brand">Every Plain Polymer</p>
      <p class="product-name">Drunkards Path</p>
      <p class="product-size">7” &amp; 3.5” set</p>
      <p class="piece-count">4 piece set</p>
    </div>
  </section>

</main>
</body>
</html>
```